SUMMIT PAVING & EARTHWORKS

I would like the front of the card to have my logo centred.
I need it to have my contact details on the back of the card which are: SummitPavingEarthworks@brindlemail.com
0413862574
and a Facebook icon

```html
<!DOCTYPE html>
<html lang="en">
<head>
<meta charset="utf-8">
<title>Summit Paving &amp; Earthworks – Business Card</title>
<link rel="stylesheet" href="https://fonts.googleapis.com/css2?family=Montserrat:wght@500;700;800&family=Arimo:wght@400&display=swap">
<style>
  :root {
    --backdrop: #e4e4e2;
    --card-white: #ffffff;
    --card-dark: #2f2f30;
    --emboss-light: #6e6e70;
    --emboss-dark: #1c1c1d;
    --brand-blue: #1c78c4;
    --ink: #2b2b2b;
    --muted-line: #3a3a3a;
    --icon-blue: #1f5fa8;
  }
  * { box-sizing: border-box; margin: 0; padding: 0; }
  html, body {
    width: 1200px; height: 801px; overflow: hidden;
    background: var(--backdrop);
  }
  .stage {
    position: relative; width: 1200px; height: 801px;
    display: flex; align-items: center; justify-content: center; gap: 50px;
  }
  .card {
    width: 530px; height: 303px; position: relative; overflow: hidden;
    box-shadow: 0 6px 18px rgba(0,0,0,0.18);
  }
  .card--front { background: var(--card-white); }
  .card--back { background: var(--card-dark); }

  .brand {
    display: flex; align-items: center; gap: 12px;
    font-family: "Montserrat", sans-serif; font-weight: 800;
    color: var(--brand-blue); letter-spacing: 0.5px; white-space: nowrap;
  }
  .brand__mark { width: 34px; height: 34px; background: var(--brand-blue); flex: none; }
  .card--front .brand {
    position: absolute; top: 58px; left: 0; right: 0;
    justify-content: center; font-size: 22px;
  }

  .details {
    position: absolute; left: 0; right: 0; top: 150px;
    display: flex; align-items: center; justify-content: center;
  }
  .person { text-align: right; padding-right: 16px; white-space: nowrap; }
  .person__name {
    font-family: "Montserrat", sans-serif; font-weight: 700; font-size: 17px;
    color: var(--brand-blue); letter-spacing: 0.5px;
  }
  .person__role {
    font-family: "Arimo", sans-serif; font-size: 15px; color: var(--ink); margin-top: 2px;
  }
  .divider { width: 1px; height: 68px; background: var(--muted-line); flex: none; }
  .contacts { list-style: none; padding-left: 14px; }
  .contacts li {
    display: flex; align-items: center; gap: 8px; white-space: nowrap;
    font-family: "Arimo", sans-serif; font-size: 12.5px; color: var(--ink);
    line-height: 21px;
  }
  .contacts svg { width: 13px; height: 13px; flex: none; }
  .icon-social { width: 13px; height: 13px; background: var(--icon-blue); border-radius: 3px; flex: none; }

  .emblem-area {
    position: absolute; left: 34px; top: 22px; width: 180px; height: 180px;
    background: linear-gradient(135deg, var(--emboss-dark) 0%, #3a3a3c 55%, var(--emboss-light) 100%);
  }
  .card--back .brand {
    position: absolute; right: 30px; bottom: 42px; font-size: 23px;
  }
</style>
</head>
<body>
<main class="stage">
  <section class="card card--front" aria-label="Card front">
    <div class="brand"><span class="brand__mark"></span>SUMMIT PAVING &amp; EARTHWORKS</div>
    <div class="details">
      <div class="person">
        <p class="person__name">DANIEL MORROW</p>
        <p class="person__role">Manager</p>
      </div>
      <div class="divider"></div>
      <ul class="contacts">
        <li>
          <svg viewBox="0 0 16 16" aria-hidden="true"><path d="M4 1.5l2.3 3-1.4 1.6c.9 2 2.5 3.6 4.5 4.5l1.6-1.4 3 2.3-1.4 2.5C7.2 14.2 1.8 8.8 1.5 3z" fill="var(--icon-blue)"/></svg>
          0413862574
        </li>
        <li>
          <svg viewBox="0 0 16 16" aria-hidden="true"><rect x="1.5" y="3.5" width="13" height="9" fill="none" stroke="var(--icon-blue)" stroke-width="1.5"/><path d="M1.5 3.5L8 9l6.5-5.5" fill="none" stroke="var(--icon-blue)" stroke-width="1.5"/></svg>
          SummitPavingEarthworks@brindlemail.com
        </li>
        <li>
          <span class="icon-social" role="img" aria-label="Social page"></span>
          @SummitPavingEarthworks
        </li>
      </ul>
    </div>
  </section>

  <section class="card card--back" aria-label="Card back">
    <div class="emblem-area" role="img" aria-label="Large embossed brand emblem area"></div>
    <div class="brand">SUMMIT PAVING &amp; EARTHWORKS</div>
  </section>
</main>
</body>
</html>
```